Web form face-lift for an online startup

We are a web startup building a SaaS application for the freight industry. The project is mainly dedicated to the paint the main form that our customer are using along the search results that the they get. All details are in the attached documents.
Updates
The application serves the Freight Forwarders community so please think towards this industry when using background images, banners, colors, icons, etc. Computer and technology images are irrelevant.
Customer fields at the top of the page is actually part of the form.
Target Market(s)
Usually business users (Sales people, procurement, shippers, freight forwarders). Some are less tech savvy and some appreciate the new trendy web apps.
Industry/Entity Type
Building
Colors
Designer to choose colors to be used in the design.
Look and feel
Each slider illustrates characteristics of the customer's brand and the style your logo design should communicate.

```html
<!DOCTYPE html>
<html lang="en">
<head>
<meta charset="utf-8">
<title>Tideway – Search For Quotes</title>
<link href="https://fonts.googleapis.com/css2?family=Roboto:wght@300;400;500;700&family=Roboto+Condensed:wght@400;700&display=swap" rel="stylesheet">
<style>
:root{
  --teal:#1aa3a0;
  --teal-dark:#2b7673;
  --header:#393939;
  --header-deep:#2d2d2d;
  --band:#3c3c3c;
  --text-light:#e8e8e8;
  --text-dark:#3a3a3a;
  --white:#ffffff;
}
*{box-sizing:border-box;margin:0;padding:0}
html,body{width:1200px;height:921px;overflow:hidden;background:var(--white)}
body{font-family:"Roboto",Arial,sans-serif;position:relative;color:var(--text-dark)}
.abs{position:absolute}

/* header */
.site-header{position:absolute;left:0;top:0;width:1200px;height:89px;background:var(--header)}
.brand{position:absolute;left:170px;top:31px;font-weight:400;font-size:21px;letter-spacing:.3px;color:var(--text-light)}
.nav-mark{position:absolute;left:419px;top:38px;width:20px;height:20px;border:2px solid var(--teal);border-radius:50%}
.main-nav{position:absolute;top:41px;left:0;font-size:12px;color:var(--text-light)}
.main-nav span{position:absolute;white-space:nowrap}
.util{position:absolute;top:8px;font-size:9px;color:var(--text-light)}
.nav-rule{position:absolute;left:415px;top:86px;width:785px;height:3px;background:var(--teal)}
.user-panel{position:absolute;left:903px;top:0;width:129px;height:86px;background:var(--header-deep)}
.avatar{position:absolute;left:40px;top:8px;width:49px;height:49px;border-radius:50%;background:linear-gradient(160deg,#8a8a8a,#4a4a4a)}
.user-name{position:absolute;left:22px;top:62px;font-size:12px;font-weight:500;color:var(--white);white-space:nowrap}
.user-caret{position:absolute;left:108px;top:66px;width:0;height:0;border-left:6px solid transparent;border-right:6px solid transparent;border-top:6px solid var(--teal)}

/* hero */
.hero{position:absolute;left:0;top:89px;width:1200px;height:258px;
  background:radial-gradient(ellipse 300px 120px at 560px 60px,rgba(200,220,220,.45),transparent),
  radial-gradient(ellipse 260px 160px at 1000px 160px,rgba(60,150,150,.55),transparent),
  radial-gradient(ellipse 260px 160px at 130px 120px,rgba(40,110,110,.5),transparent),
  linear-gradient(90deg,#0e2424,#1d3b3b 40%,#223e40 70%,#153133)}
.hero-title{position:absolute;left:173px;top:145px;font-size:19px;font-weight:300;color:var(--white)}
.label-light{position:absolute;font-size:13px;font-weight:300;color:var(--text-light);white-space:nowrap}
.field-dark{position:absolute;border:1px solid #9aa;background:rgba(0,0,0,.15)}
.check{position:absolute;width:11px;height:11px;border-radius:2px;background:linear-gradient(#fafafa,#c8c8c8);border:1px solid #999}
.mode-tab{position:absolute;background:#3c3c3c;display:flex;align-items:center;justify-content:center}
.mode-tab.active{background:#464646}

/* cargo band */
.cargo-band{position:absolute;left:0;top:347px;width:1200px;height:133px;background:var(--band)}
.input-dark{position:absolute;height:27px;border:1px solid #bbb;color:var(--white);font-size:12px;display:flex;align-items:center;justify-content:center;font-weight:300}
.unit-select{position:absolute;height:27px;background:var(--teal-dark);color:var(--white);font-size:13px;font-weight:500}
.unit-select .val{position:absolute;left:10px;top:5px}
.unit-select .div{position:absolute;top:0;width:1px;height:27px;background:#1f5755}
.caret-w{position:absolute;top:12px;width:0;height:0;border-left:4px solid transparent;border-right:4px solid transparent;border-top:5px solid var(--white)}
.add-units{position:absolute;left:169px;top:438px;width:129px;height:25px;background:var(--teal-dark);color:var(--white);font-size:12px;font-weight:500}

/* route */
.route{position:absolute;left:0;top:480px;width:1200px;height:53px;border-top:1px solid #ccc;border-bottom:1px solid #ddd}
.route-label{position:absolute;top:21px;font-size:12px;font-weight:500;color:var(--text-dark)}
.input-light{position:absolute;top:12px;height:31px;width:332px;border:1px solid #b9b9b9;font-size:12px;font-weight:300;color:#555;padding:8px 10px}

/* options */
.options-title{position:absolute;left:169px;top:569px;font-size:27px;font-weight:300;color:var(--text-dark)}
.trade{position:absolute;top:624px;font-size:16px;font-weight:300;color:var(--text-dark);white-space:nowrap}
.trade .accent{color:var(--teal)}
.sep{position:absolute;top:630px;height:12px;border-left:1px dotted #999}
.price-select{position:absolute;left:678px;top:618px;width:353px;height:34px;border:1px solid #bbb;font-size:13px;font-weight:300;color:#444}
.more-option{position:absolute;left:939px;top:660px;font-size:13px;font-weight:300;color:#555;white-space:nowrap}
.search-btn{position:absolute;left:494px;top:725px;width:214px;height:38px;background:var(--teal-dark);color:var(--white);font-family:"Roboto Condensed",Arial,sans-serif;font-size:21px;display:flex;align-items:center;justify-content:center}
.alt{position:absolute;left:494px;width:214px;text-align:center;font-size:13px;font-weight:300;color:#444}

/* footer */
.site-footer{position:absolute;left:0;top:857px;width:1200px;height:64px;background:var(--header)}
.footer-link{position:absolute;top:26px;font-size:13px;font-weight:300;color:#ccc;white-space:nowrap}
.social{position:absolute;top:21px;width:22px;height:22px;border-radius:50%;background:#8f8f8f}
</style>
</head>
<body>

<header class="site-header">
  <div class="brand">Tideway</div>
  <div class="nav-mark"></div>
  <nav class="main-nav">
    <span style="left:460px">Menu Item 1</span>
    <span style="left:547px">Menu Item 2</span>
    <span style="left:633px">Menu Item 3</span>
    <span style="left:720px">Menu Item 4</span>
    <span style="left:806px">Menu Item 5</span>
  </nav>
  <span class="util" style="left:790px">USD</span>
  <span class="util" style="left:837px">ENGLISH</span>
  <div class="user-panel">
    <div class="avatar" role="img" aria-label="User profile photo"></div>
    <div class="user-name">DANA MERCER</div>
    <div class="user-caret"></div>
  </div>
</header>
<div class="nav-rule"></div>

<section class="hero" role="img" aria-label="Blurred photo of a container port in teal tones"></section>
<div class="hero-title">Search For Quotes</div>
<span class="label-light" style="left:173px;top:181px">Customer</span>
<div class="field-dark" style="left:240px;top:178px;width:212px;height:27px"></div>
<div class="check" style="left:172px;top:238px"></div>
<span class="label-light" style="left:193px;top:236px">Rate A Quote ?</span>

<div class="mode-tab active" style="left:498px;top:268px;width:93px;height:79px">
  <svg width="74" height="62" viewBox="0 0 74 62" fill="none" stroke="#b5b5b5" stroke-width="5" stroke-linejoin="round">
    <path d="M8 18 L37 6 L66 18 L37 30 Z"/><path d="M8 18 V44 L37 56 L66 44 V18"/><path d="M37 30 V56"/>
  </svg>
</div>
<div class="mode-tab" style="left:597px;top:285px;width:93px;height:62px">
  <svg width="62" height="48" viewBox="0 0 62 48" fill="#b5b5b5">
    <rect x="14" y="6" width="6" height="14"/><rect x="24" y="14" width="32" height="14"/>
    <path d="M2 26 H60 L54 44 H8 Z"/><circle cx="20" cy="35" r="2" fill="#3c3c3c"/><circle cx="28" cy="35" r="2" fill="#3c3c3c"/>
  </svg>
</div>
<div class="mode-tab" style="left:697px;top:285px;width:93px;height:62px">
  <svg width="48" height="48" viewBox="0 0 48 48" fill="#b5b5b5">
    <path d="M24 4 L42 13 L24 22 L6 13 Z"/><path d="M4 16 L22 25 V44 L4 35 Z"/><path d="M44 16 L26 25 V44 L44 35 Z"/>
  </svg>
</div>

<section class="cargo-band">
  <span class="label-light" style="left:172px;top:28px">Qty</span>
  <span class="label-light" style="left:253px;top:28px">Stackable</span>
  <span class="label-light" style="left:341px;top:27px">Load</span>
  <span class="label-light" style="left:577px;top:28px">Length</span>
  <span class="label-light" style="left:651px;top:28px">Width</span>
  <span class="label-light" style="left:728px;top:28px">Height</span>
  <span class="label-light" style="left:888px;top:28px">Weight</span>
</section>
<div class="input-dark" style="left:170px;top:393px;width:48px;font-weight:400">5</div>
<div class="check" style="left:254px;top:400px"></div>
<div class="input-dark" style="left:339px;top:393px;width:220px;justify-content:flex-start;padding-left:8px;font-size:10px;font-weight:400">Box / Pallet</div>
<div class="abs" style="left:534px;top:406px;border-left:6px solid transparent;border-right:6px solid transparent;border-top:6px solid var(--teal)"></div>
<div class="input-dark" style="left:575px;top:395px;width:59px">100</div>
<div class="input-dark" style="left:650px;top:395px;width:59px">100</div>
<div class="input-dark" style="left:724px;top:395px;width:59px">100</div>
<div class="unit-select" style="left:791px;top:395px;width:75px"><span class="val">cm</span><span class="div" style="left:49px"></span><span class="caret-w" style="left:59px"></span></div>
<div class="input-dark" style="left:883px;top:395px;width:59px">100</div>
<div class="unit-select" style="left:953px;top:395px;width:78px"><span class="val" style="left:15px">kg</span><span class="div" style="left:51px"></span><span class="caret-w" style="left:62px"></span></div>
<div class="add-units">
  <svg class="abs" style="left:9px;top:6px" width="13" height="13" viewBox="0 0 13 13" fill="none" stroke="#fff" stroke-width="1.2"><circle cx="6.5" cy="6.5" r="5.8"/><path d="M6.5 3.5v6M3.5 6.5h6"/></svg>
  <span class="abs" style="left:33px;top:5px">Add more units</span>
</div>

<section class="route">
  <span class="route-label" style="left:170px">From :</span>
  <div class="input-light" style="left:213px">Shipping address or port</div>
  <svg class="abs" style="left:589px;top:16px" width="22" height="22" viewBox="0 0 22 22" fill="none" stroke="#333" stroke-width="1.2"><circle cx="11" cy="11" r="10"/><path d="M9 6l5 5-5 5"/></svg>
  <span class="route-label" style="left:655px">To :</span>
  <div class="input-light" style="left:698px">Shipping address or port</div>
</section>

<h2 class="options-title">Options</h2>
<span class="trade" style="left:169px">Import</span>
<span class="sep" style="left:227px"></span>
<span class="trade" style="left:237px">Export</span>
<span class="sep" style="left:293px"></span>
<span class="trade" style="left:304px">Incoterm <span class="accent">: FCA</span></span>

<div class="check" style="left:487px;top:630px"></div>
<svg class="abs" style="left:506px;top:624px" width="22" height="22" viewBox="0 0 22 22" fill="none" stroke="#d0202a" stroke-width="2"><circle cx="11" cy="11" r="9.5"/><rect x="7" y="6" width="8" height="10" stroke="#333" stroke-width="1.2"/><path d="M4 18L18 4"/></svg>
<div class="check" style="left:549px;top:630px"></div>
<svg class="abs" style="left:569px;top:624px" width="22" height="22" viewBox="0 0 22 22" fill="none" stroke="#d0202a" stroke-width="2"><circle cx="11" cy="11" r="9.5"/><path d="M7 16h8M11 6v10" stroke="#333" stroke-width="1.6"/><path d="M4 18L18 4"/></svg>
<div class="check" style="left:609px;top:630px"></div>
<svg class="abs" style="left:628px;top:624px" width="22" height="22" viewBox="0 0 22 22" fill="none" stroke="#d0202a" stroke-width="2"><circle cx="11" cy="11" r="9.5"/><circle cx="11" cy="11" r="4" fill="#333" stroke="none"/><path d="M4 18L18 4"/></svg>

<div class="price-select">
  <span class="abs" style="left:12px;top:10px">Price Level</span>
  <span class="abs" style="left:317px;top:0;width:1px;height:32px;background:#ccc"></span>
  <span class="abs" style="left:328px;top:14px;border-left:6px solid transparent;border-right:6px solid transparent;border-top:6px solid var(--teal)"></span>
</div>
<div class="more-option">
  <svg class="abs" style="left:0;top:1px" width="17" height="17" viewBox="0 0 17 17" fill="none" stroke="#2b7673" stroke-width="1.3"><circle cx="8.5" cy="8.5" r="7.5"/><path d="M8.5 5v7M5 8.5h7"/></svg>
  <span style="margin-left:22px">more option</span>
</div>

<div class="search-btn">SEARCH QUOTES</div>
<div class="alt" style="top:774px">or</div>
<div class="alt" style="top:790px">Create manually</div>

<footer class="site-footer">
  <span class="footer-link" style="left:171px">About Us</span>
  <span class="footer-link" style="left:245px">Privacy Policy</span>
  <span class="footer-link" style="left:350px">Terms Of service</span>
  <span class="footer-link" style="left:473px">News</span>
  <span class="social" style="left:881px"></span>
  <span class="social" style="left:913px"></span>
  <span class="social" style="left:944px"></span>
  <span class="social" style="left:975px"></span>
  <span class="social" style="left:1007px"></span>
</footer>

</body>
</html>
```